Clean & Inspiring Web Design Project

Larkspur Prototype Studio, LLC (also known as LP-Studio) is a company which provides 3D printing services and products. The emphasis is on making these products and services available to the mass-market - customers and users who may or may not have prior experience with 3D printing and/or rapid prototyping technologies. We are a start-up company, looking to build a clean and creativity inspiring brand - our site must encourage visitor to engage and make something. Our aim is to help take mere ideas and turn them into tangible items. We want to show a fusion of ideas (e.g. pencil sketches on graph paper) with design tools (e.g. CAD and drafting software) and rapid prototyping (e.g. TinkNod 3D printers, Stereolithography Machines, etc.). We would like the website to appear professional but at the same time easy to navigate and a good balance between text and pictures. The final design should inspire customers to nurture their ideas into real products and communicate our services to our customers. Our site should have the feel of a vibrant social community with the added benefit of tangible physical creations.

Target Market(s)

People with great ideas that need to be designed into a real product

Industry/Entity Type

Printing

Requirements
Must have
• - Website design should include 2 layouts - one for a "landing page" and one for a "content page"
- Website design must incorporate attached company logo (or derivative of this logo)
- Website design should incorporate the menu options shown in the attached PDF UI concept (UI does not necessarily need to look like the provided concept, just include all the clickable elements)
- Website design must portray an innovative and cooperative design environment with a look-and-feel that appeals to both amateur and professional designers.
- Please include pictures, illustrations and photographs (as needed) related to 3D printing, CAD design, conventional drafting, engineering and manufacturing industries.
- Design should support scaling to multiple screen sizes, from tablet computers (e.g. Slabix) to very large screen PCs.
- Design should include Username & Password fields for login or a button to pull up a login popup.
Nice to have
• - Website design could include "Invent", "Make", "Produce" and "Buy" options that slowly cycle through - with appropriate photos / graphics. These "menu options" would also be mouse-over enabled to switch into the appropriate context as the cursor enters that region (e.g. mouse over the "Invent" text would bring up page 2, etc.). (See attached Original UI Thoughts)
Should not have
• Requirements - Should Not Have:
- Website design should not portray a service that is very expensive or complicated - we are a reasonably priced service meant to be friendly with amateur inventors
- Website design should not be overly complicated - please keep it reasonably simple
- Website design should not be overly trendy
- Website design should not use more than 2 font styles, gaudy fonts, etc.
- Website design should not be "campy" or "tacky" - playful is ok, but please keep it elegant
- Website design should not be overly masculine or feminine - we will have both women and men as customers

```html
<!DOCTYPE html>
<html lang="en">
<head>
<meta charset="utf-8">
<title>Larkspur Prototype Studio</title>
<link href="https://fonts.googleapis.com/css2?family=PT+Sans:wght@400;700&family=Arimo:wght@400;700&display=swap" rel="stylesheet">
<style>
:root{
  --blue:#1f6fb5;
  --blue-dark:#0f4f8c;
  --blue-light:#5ab4ee;
  --sky:#29b6ee;
  --orange:#f7941d;
  --orange-light:#ffb347;
  --text:#555;
  --footer:#45403d;
  --footer-text:#e8e4e0;
  --line:#d8dde3;
}
*{margin:0;padding:0;box-sizing:border-box}
html,body{width:1060px;height:1200px;overflow:hidden}
body{position:relative;background:linear-gradient(#f5f5f5,#fff 700px);font-family:"PT Sans",sans-serif;color:var(--text)}
.abs{position:absolute}

/* header */
.brand{left:77px;top:13px;display:flex;align-items:center;gap:18px}
.brand-mark{width:66px;height:74px;background:var(--blue);border-radius:6px}
.brand-name{font-size:22px;color:var(--blue);line-height:1.1}
.brand-tag{font-size:13px;color:var(--blue);margin-top:5px}
.cart{left:838px;top:22px;font-size:14px;color:#444;display:flex;align-items:center;gap:6px}
.search{left:745px;top:58px;width:237px;height:27px;border:1px solid #ccc;border-radius:14px;background:#fff;overflow:hidden;display:flex}
.search span{flex:1;font-size:14px;color:#555;padding:4px 12px}
.search b{width:31px;background:linear-gradient(var(--blue-light),var(--blue));color:#fff;font-weight:400;font-size:12px;text-align:center;line-height:27px}

/* nav */
.nav{left:0;top:100px;width:1060px;height:47px;background:linear-gradient(#6cc4f4,#2a8fd8 55%,#1f78c4)}
.nav a{position:absolute;top:10px;height:30px;line-height:30px;color:#fff;font-size:15px;text-decoration:none;transform:translateX(-50%)}
.nav a.active{left:120px;width:86px;text-align:center;background:var(--blue-dark);border-radius:4px;border:1px solid #0b3c6a}
.nav i{position:absolute;top:12px;width:1px;height:24px;background:rgba(255,255,255,.55)}

/* slider */
.slider{left:78px;top:159px;width:902px;height:424px;background:#fff}
.banner{left:20px;top:20px;width:861px;height:382px;background:linear-gradient(110deg,#1ec0f2,#2a9be0 45%,#1c6fba);overflow:hidden}
.banner h1{position:absolute;left:50px;top:86px;font-size:28px;font-weight:400;color:#fff}
.banner p{position:absolute;left:50px;top:137px;width:385px;font-size:14px;line-height:21px;color:#fff}
.btn{background:linear-gradient(var(--orange-light),var(--orange));color:#fff;font-weight:700;border-radius:5px;text-align:center;border:1px solid #e98a10}
.banner .btn{position:absolute;left:50px;top:261px;width:118px;height:38px;line-height:36px;font-size:16px;border-radius:8px}
.frame{left:473px;top:31px;width:383px;height:323px;background:#fff;padding:6px}
.photo{width:100%;height:100%}
.arrow{top:345px;width:34px;height:34px;border-radius:50%;background:#1d1d1d}
.dots{left:478px;top:580px;width:110px;height:28px;background:#f2f2f2;border:1px solid #ddd;border-top:none;border-radius:0 0 6px 6px;display:flex;justify-content:center;align-items:center;gap:9px}
.dots i{width:9px;height:9px;border-radius:50%;background:#c9c9c9}
.dots i.on{background:var(--orange)}

/* cards */
.card{top:639px;width:289px;height:258px;background:#fff;border:1px solid var(--line);border-radius:8px;overflow:hidden}
.card h2{height:38px;background:linear-gradient(#5fb7ee,#1e78c6);color:#fff;font-size:16px;line-height:38px;padding-left:21px}
.card .photo{margin:15px 0 0 18px;width:254px;height:80px}
.card p{margin:12px 14px 0 20px;font-size:12.5px;line-height:16px;text-align:justify}
.card p strong{color:#555}
.card .btn{position:absolute;right:17px;bottom:15px;width:79px;height:25px;line-height:23px;font-size:12px}

/* footer */
.footer{left:0;top:927px;width:1060px;height:273px;background:var(--footer);color:var(--footer-text);font-family:"Arimo",sans-serif}
.f-brand{left:75px;top:42px;display:flex;gap:12px}
.f-brand .brand-mark{width:48px;height:54px}
.f-brand .name{font-size:16px;color:#fff}
.f-brand .tag{font-size:12px;color:#aaa;margin-top:6px}
.footer h3{position:absolute;top:24px;font-weight:400;font-size:16px;color:#fff}
.vline{top:59px;width:1px;height:154px;background:#777}
.contact{left:352px;display:flex;align-items:center;gap:13px;font-size:11px}
.ico{width:27px;height:27px;border-radius:50%;background:var(--orange);display:flex;align-items:center;justify-content:center}
.links{left:548px;top:58px;list-style:none;font-size:11px;line-height:23px}
.links li::before{content:"›";margin-right:7px;font-size:13px}
.email{left:727px;top:55px;width:203px;height:30px;background:#fff;border:1px solid #bbb;border-radius:3px;font-size:11px;color:#aaa;padding:8px 9px}
.footer .btn{left:727px;top:99px;width:79px;height:26px;line-height:24px;font-size:12px;font-family:"PT Sans",sans-serif}
.social{left:75px;top:213px;display:flex;gap:12px}
.social i{width:32px;height:32px;border-radius:50%;background:var(--orange);display:block}
.bottom{right:77px;top:213px;text-align:right;font-size:11px;line-height:16px}
</style>
</head>
<body>

<header>
  <div class="abs brand">
    <div class="brand-mark"></div>
    <div><div class="brand-name">Larkspur Prototype Studio</div><div class="brand-tag">What you want...Now!</div></div>
  </div>
  <div class="abs cart">
    <svg width="22" height="18" viewBox="0 0 22 18" fill="none" stroke="#333" stroke-width="1.6"><path d="M1 2h4l2 10h11l2-8H6"/><circle cx="9" cy="16" r="1.3"/><circle cx="17" cy="16" r="1.3"/></svg>
    View Shopping Cart
  </div>
  <div class="abs search"><span>Search</span><b>Go</b></div>
</header>

<nav class="abs nav">
  <a class="active" href="#">About LP</a>
  <i style="left:180px"></i>
  <a href="#" style="left:235px">Dream</a>
  <i style="left:286px"></i>
  <a href="#" style="left:340px">Make</a>
  <i style="left:392px"></i>
  <a href="#" style="left:449px">Produce</a>
  <i style="left:512px"></i>
  <a href="#" style="left:562px">Sell</a>
</nav>

<section class="abs slider">
  <div class="abs banner">
    <h1>Lorem Lipsum Dolor Sit Amet</h1>
    <p>Lorem ipsum dolorsit amet, consectetur adipiscing elit. VesEbulum bibendum posuere dolor, nec egestas odio auctor eget. Suspendisse interdum lacinia sagiGs. Nunc nibh lectus, elementum eget loborEs commodo, fringilla rhoncus neque. Suspendisse at lectus arcuuspendis...</p>
    <div class="btn">Read More</div>
    <div class="abs frame"><div class="photo" role="img" aria-label="Photo of a glowing 3D printed lattice lamp on a dark background" style="background:radial-gradient(circle at 40% 40%,#c9a875,#5a4526 45%,#000 75%)"></div></div>
  </div>
  <div class="abs dots"><i class="on"></i><i></i><i></i><i></i><i></i></div>
</section>
<svg class="abs arrow" style="left:19px" viewBox="0 0 34 34"><circle cx="17" cy="17" r="17" fill="#1d1d1d"/><path d="M20 10l-8 7 8 7z" fill="#fff"/></svg>
<svg class="abs arrow" style="left:1005px" viewBox="0 0 34 34"><circle cx="17" cy="17" r="17" fill="#1d1d1d"/><path d="M14 10l8 7-8 7z" fill="#fff"/></svg>

<section>
  <article class="abs card" style="left:78px">
    <h2>LP Store</h2>
    <div class="photo" role="img" aria-label="Photo of assorted 3D printed parts and containers" style="background:linear-gradient(90deg,#555,#d9d4cc 30%,#e8602a 45%,#6a9a8a 70%,#ddd)"></div>
    <p>when an unknown printer took a galley of type and scrambled it to make a type specimen book. when an unknown printer took a galley of type and scrambled it to make a type specimen.</p>
    <div class="btn">Read More</div>
  </article>
  <article class="abs card" style="left:386px">
    <h2>LP Printers</h2>
    <div class="photo" role="img" aria-label="Photo of a 3D printed lattice high-heel shoe" style="background:linear-gradient(90deg,#8a7a70,#c7b3a6 40%,#3a3330 70%,#b5a9a0)"></div>
    <p>when an unknown printer took a galley of type and scrambled it to make a type specimen book. when an unknown printer took a galley of type and scrambled it to make a type specimen.</p>
    <div class="btn">Read More</div>
  </article>
  <article class="abs card" style="left:695px">
    <h2>Blog</h2>
    <div class="photo" role="img" aria-label="Photo of a 3D printed organic lattice sculpture" style="background:radial-gradient(circle at 50% 50%,#e9e2d2,#9b8f7a 50%,#3c3428)"></div>
    <p><strong>When an unknown printer took</strong><br>Srambled it to make a type specimen book. when an unknown printer took a galley of type and scrambled it to make a type specimen.</p>
    <div class="btn">Read More</div>
  </article>
</section>

<footer class="abs footer">
  <div class="abs f-brand">
    <div class="brand-mark"></div>
    <div><div class="name">Larkspur Prototype Studio</div><div class="tag">What You Want..... Now!</div></div>
  </div>

  <div class="abs vline" style="left:343px"></div>
  <h3 style="left:352px">Contact Us</h3>
  <div class="abs contact" style="top:64px"><span class="ico"><svg width="14" height="14" viewBox="0 0 14 14"><path d="M3 1l2 3-1 2c1 2 2 3 4 4l2-1 3 2-1 2C6 13 1 8 1 2z" fill="#fff"/></svg></span>(123) 456 789</div>
  <div class="abs contact" style="top:113px"><span class="ico"><svg width="14" height="10" viewBox="0 0 14 10"><rect width="14" height="10" rx="1" fill="#fff"/><path d="M0 1l7 5 7-5" stroke="#f7941d" fill="none"/></svg></span>hello@larkspurstudio.com</div>
  <div class="abs contact" style="top:161px"><span class="ico"><svg width="15" height="13" viewBox="0 0 15 13"><path d="M7.5 0L0 6.5h2V13h4V9h3v4h4V6.5h2z" fill="#fff"/></svg></span>Address Comes Here</div>

  <div class="abs vline" style="left:533px"></div>
  <h3 style="left:546px">Quick Links</h3>
  <ul class="abs links"><li>About LP</li><li>Dream</li><li>Make</li><li>Produce</li><li>Sell</li><li>Contact</li></ul>

  <h3 style="left:726px">Newsletter</h3>
  <div class="abs email">Enter your email address</div>
  <div class="abs btn">Submit</div>

  <div class="abs social">
    <i role="img" aria-label="Chirpline"></i><i role="img" aria-label="Linkwork"></i><i role="img" aria-label="Facefold"></i><i role="img" aria-label="Email"></i><i role="img" aria-label="ViewTube"></i>
  </div>
  <div class="abs bottom">Home &nbsp;|&nbsp; Contact &nbsp;|&nbsp; Frenchise &nbsp;|&nbsp; Distributors &nbsp;|&nbsp; Cart<br>© &nbsp;2012 Larkspur Prototype Studio. All rights reserved.</div>
</footer>

</body>
</html>
```